seeking a modern Business Card design for Roof Plumbering Business

wexcombe roof plumbing is a local metal re-roof and new construction specialist. We are seeking a modern business card to assist with networking within the industry. Our services are predominantly the installation of metal roofs on new houses, however we also do re-roofs when an existing roof needs replacing. We service both residential and commercial properties. Please include the below details on the card:
Name: Owen Wexcombe
Phone: 0471 385 962
Email: owenwexcomberoofing@mailnest.example

Residential & Commercial
Re-roof & New Construction
Fully Insured

I have uploaded our business logo, which we think would suit a black background. Please use all lower case for business name.
Cheers
Updates

Hey Guys, As requested I've uploaded a Pdf version of my logo. Hopefully this help. Thanks

Industry/Entity Type

Business

Contact Information for Business Card

Name: Owen Wexcombe
Phone: 0471 385 962

Residential & Commercial
Fully Insured

Font styles to use
Serif
Sans Serif

Requirements
Must have
• Name must be all lower case "wexcombe roof plumbing"
Nice to have
• Stick with Logo Colours

```html
<!DOCTYPE html>
<html lang="en">
<head>
<meta charset="utf-8">
<title>wexcombe roof plumbing — business card</title>
<link rel="stylesheet" href="https://fonts.googleapis.com/css2?family=Montserrat:wght@400;600&display=swap">
<style>
  :root {
    --page: #e9e6e1;
    --card: #0b0b0c;
    --card-sheen: #1c1c1f;
    --accent: #2bb8dc;
    --icon: #8a8f94;
  }
  * { box-sizing: border-box; margin: 0; padding: 0; }
  html, body {
    width: 1200px;
    height: 1022px;
    overflow: hidden;
    background: var(--page);
  }
  .canvas {
    width: 1200px;
    height: 1022px;
    display: flex;
    align-items: center;
    justify-content: center;
  }
  .business-card {
    position: relative;
    width: 900px;
    height: 514px;
    background: linear-gradient(120deg, var(--card) 0%, var(--card-sheen) 45%, var(--card) 75%);
    box-shadow: 0 18px 40px rgba(0,0,0,0.35);
    font-family: "Montserrat", Arial, sans-serif;
    color: var(--accent);
  }
  .brand {
    position: absolute;
    left: 70px;
    top: 318px;
    display: flex;
    align-items: center;
    gap: 14px;
  }
  .brand-mark {
    width: 14px;
    height: 14px;
    background: var(--accent);
    flex: none;
  }
  .brand-name {
    font-size: 24px;
    font-weight: 400;
    line-height: 1;
    letter-spacing: 0.5px;
    color: var(--accent);
    white-space: nowrap;
  }
  .contact {
    position: absolute;
    left: 480px;
    top: 92px;
    width: 400px;
  }
  .contact-name {
    font-size: 27px;
    font-weight: 600;
    letter-spacing: 1px;
    text-transform: uppercase;
    margin-bottom: 16px;
  }
  .contact-line {
    display: flex;
    align-items: center;
    gap: 10px;
    font-size: 15px;
    font-weight: 400;
    line-height: 1.65;
    white-space: nowrap;
  }
  .contact-line svg { flex: none; }
  .services {
    margin-top: 30px;
    list-style: none;
    padding-left: 24px;
  }
  .services li {
    font-size: 17px;
    line-height: 1.55;
    letter-spacing: 0.3px;
  }
</style>
</head>
<body>
<main class="canvas">
  <article class="business-card">
    <div class="brand">
      <span class="brand-mark" aria-hidden="true"></span>
      <span class="brand-name">wexcombe roof plumbing</span>
    </div>

    <section class="contact">
      <h1 class="contact-name">Owen Wexcombe</h1>
      <p class="contact-line">
        <svg width="14" height="14" viewBox="0 0 24 24" aria-hidden="true"><path fill="var(--icon)" d="M6.6 10.8a15.1 15.1 0 0 0 6.6 6.6l2.2-2.2a1 1 0 0 1 1-.25 11.4 11.4 0 0 0 3.6.57 1 1 0 0 1 1 1V20a1 1 0 0 1-1 1A17 17 0 0 1 3 4a1 1 0 0 1 1-1h3.5a1 1 0 0 1 1 1c0 1.25.2 2.450.57 3.57a1 1 0 0 1-.25 1z"/></svg>
        0471 385 962
      </p>
      <p class="contact-line">
        <svg width="14" height="14" viewBox="0 0 24 24" aria-hidden="true"><rect x="2" y="5" width="20" height="14" rx="1.5" fill="none" stroke="var(--icon)" stroke-width="2"/><path d="M3 6l9 7 9-7" fill="none" stroke="var(--icon)" stroke-width="2"/></svg>
        owenwexcomberoofing@mailnest.example
      </p>
      <ul class="services">
        <li>Residential &amp; Commercial</li>
        <li>Re-roof &amp; New Construction</li>
        <li>Fully Insured</li>
      </ul>
    </section>
  </article>
</main>
</body>
</html>
```